Business Card Design Project

Business card design for an IT Service company. A logo has already been created in a different contest and has been attached to this project. Ideally we're looking for a double sided business card that matches the look and feel of our newly created logo.

We're open to creativity if you feel a tag line is needed such as "IT Services and Application Development". We're open to really and look and feel - even single sided business cards if you feel you have something that's a great idea.

Last thought here - I'm not sure how it'll look but maybe a two tone card? One side dark blue and the other side white? Don't limit the design submissions to this tho - just curious if it would look good

Nothing too busy please - simple... Thank you and happy designing!

Target Market(s)

Businesses that require IT Services and support for hosted services, technical consultation, web design.

Industry/Entity Type

Business

Font styles to use
Sans Serif

Requirements
Must have
• Use the colors provided in the logo (see attachment) or additional colors that compliment
Must have the following contact info (not necessarily in this order):
- Alan Fisk
- Founding Partner
- afisk@quillbarrow.example
- 555-382-1946
- www.quillbarrow.example

```html
<!DOCTYPE html>
<html lang="en">
<head>
<meta charset="utf-8">
<title>Quillbarrow — Business Card</title>
<link rel="stylesheet" href="https://fonts.googleapis.com/css2?family=Arimo:ital,wght@0,400;0,700;1,400&display=swap">
<style>
  :root {
    --card-bg: #ffffff;
    --navy: #0f1a5a;
    --green: #5aab1e;
    --blue: #2b8be0;
  }
  * { margin: 0; padding: 0; box-sizing: border-box; }
  html, body {
    width: 1200px;
    height: 734px;
    overflow: hidden;
    background: var(--card-bg);
  }
  .card {
    position: relative;
    width: 1200px;
    height: 734px;
    background: var(--card-bg);
    font-family: "Arimo", Arial, Helvetica, sans-serif;
    color: var(--navy);
  }
  .brand {
    position: absolute;
    left: 122px;
    top: 178px;
    display: flex;
    align-items: center;
    gap: 22px;
  }
  .brand-square {
    width: 62px;
    height: 62px;
    background: var(--green);
  }
  .brand-name {
    font-size: 76px;
    font-weight: 700;
    line-height: 1;
    letter-spacing: -1px;
    color: var(--navy);
  }
  .identity {
    position: absolute;
    right: 105px;
    top: 182px;
    text-align: right;
  }
  .identity-name {
    font-size: 43px;
    font-weight: 400;
    line-height: 1.1;
  }
  .identity-role {
    font-size: 29px;
    font-weight: 400;
    line-height: 1.2;
  }
  .contact {
    position: absolute;
    left: 135px;
    right: 128px;
    top: 644px;
    display: flex;
    justify-content: space-between;
    font-size: 25px;
    line-height: 1;
  }
  .contact-label {
    font-weight: 700;
    margin-right: 8px;
  }
  .contact-value {
    font-style: italic;
  }
</style>
</head>
<body>
  <main class="card">
    <div class="brand">
      <span class="brand-square"></span>
      <span class="brand-name">Quillbarrow</span>
    </div>

    <div class="identity">
      <p class="identity-name">Alan Fisk</p>
      <p class="identity-role">Founding Partner</p>
    </div>

    <div class="contact">
      <p class="contact-item"><span class="contact-label">T</span><span class="contact-value">555-382-1946</span></p>
      <p class="contact-item"><span class="contact-label">E</span><span class="contact-value">afisk@quillbarrow.example</span></p>
      <p class="contact-item"><span class="contact-label">W</span><span class="contact-value">www.quillbarrow.example</span></p>
    </div>
  </main>
</body>
</html>
```